specialised legal consultancy business needs an update on logo and office stationary.

Update on Logo - see attached.

update on email signature - something new and fresh with only the following details -

(the logo)
Advocate Peter Sandovik
PS Entity Frameworks (Pty) Ltd (Reg No.: 2019 / 153927 / 07)
LLB, LLM (Cum Laude), Cert.Dir (KWBFE), FCG (TREPX)
+27 71 592 6604
peter#kwellbrandt.com

Update on letterhead - something new and fresh and please more user-friendly. With the same details as per the email signature.

```html
<!DOCTYPE html>
<html lang="en">
<head>
<meta charset="utf-8">
<title>PS Entity Frameworks – Stationery</title>
<link rel="stylesheet" href="https://fonts.googleapis.com/css2?family=Source+Sans+3:wght@400;600;700&display=swap">
<style>
  :root{
    --stage:#dcdcdc;
    --paper:#ffffff;
    --brand-grey:#666666;
    --ink:#111111;
    --rule:#444444;
  }
  *{margin:0;padding:0;box-sizing:border-box}
  html,body{width:1200px;height:900px;overflow:hidden;background:var(--paper)}
  body{position:relative;font-family:"Source Sans 3",Arial,sans-serif;color:var(--ink)}

  .stage-left{position:absolute;left:0;top:0;width:658px;height:900px;background:var(--stage)}

  .letterhead{position:absolute;left:32px;top:30px;width:594px;height:840px;background:var(--paper);
    box-shadow:6px 8px 14px rgba(0,0,0,.45)}
  .letterhead .wordmark{position:absolute;left:0;right:0;top:52px;text-align:center}
  .wordmark{font-weight:600;color:var(--brand-grey);text-transform:uppercase;line-height:1}
  .letterhead .wordmark span{display:block;font-size:15px;letter-spacing:1.5px}
  .letterhead .wordmark .initials{font-size:34px;letter-spacing:2px;margin-bottom:6px}

  .letterhead-footer{position:absolute;left:0;right:0;top:778px;text-align:center}
  .letterhead-footer .trading-name{font-size:9.6px}
  .letterhead-footer .contacts{margin-top:5px;font-size:8.4px;display:flex;justify-content:center;gap:11px}
  .contact{display:inline-flex;align-items:center;gap:3px}
  .contact svg{flex:none}
  .letterhead-footer .credentials{margin-top:9px;font-size:5.2px;color:#222}

  .hero-mark{position:absolute;left:780px;top:190px;width:320px;text-align:center}
  .hero-mark .initials{font-size:120px;letter-spacing:4px}
  .hero-mark .name{font-size:44px;letter-spacing:2px;margin-top:18px;display:block}

  .signature{position:absolute;left:686px;top:622px;width:485px;height:126px;background:var(--paper);
    box-shadow:3px 4px 8px rgba(0,0,0,.4);border:1px solid #e4e4e4}
  .signature .wordmark{position:absolute;left:0;top:20px;width:158px;text-align:center}
  .signature .wordmark span{display:block;font-size:13px;letter-spacing:1px}
  .signature .wordmark .initials{font-size:36px;letter-spacing:2px;margin-bottom:6px}
  .signature .divider{position:absolute;left:158px;top:10px;width:1px;height:106px;background:var(--rule)}
  .signature .details{position:absolute;left:181px;top:11px;right:6px}
  .signature .trading-name{font-size:11.4px;margin-bottom:7px}
  .signature .row{display:flex;gap:10px;font-size:9px;margin-bottom:4px}
  .signature .fine{font-size:7.7px;line-height:12.6px}
  b{font-weight:700}
</style>
</head>
<body>
  <div class="stage-left"></div>

  <section class="letterhead">
    <div class="wordmark">
      <span class="initials">PS</span>
      <span>Entity Frameworks</span>
    </div>

    <footer class="letterhead-footer">
      <p class="trading-name">P Sandovik t/a <b>PS Entity Frameworks</b></p>
      <p class="contacts">
        <span class="contact"><svg width="8" height="8" viewBox="0 0 10 10"><circle cx="5" cy="5" r="4.4" fill="none" stroke="#111" stroke-width=".9"/><path d="M3.4 2.8l1 1-.5.6a3 3 0 0 0 1.7 1.7l.6-.5 1 1-.7.7C5 7.1 2.9 5 3 3.5z" fill="#111"/></svg>+27 71 592 6604</span>
        <span class="contact"><svg width="9" height="7" viewBox="0 0 10 8"><rect x=".5" y=".5" width="9" height="7" rx="1" fill="none" stroke="#111" stroke-width=".9"/><path d="M.8 1l4.2 3.4L9.2 1" fill="none" stroke="#111" stroke-width=".9"/></svg>peter@kwellbrandt.com</span>
        <span class="contact"><svg width="7" height="9" viewBox="0 0 8 11"><path d="M4 0a4 4 0 0 0-4 4c0 3 4 7 4 7s4-4 4-7a4 4 0 0 0-4-4zm0 5.5A1.5 1.5 0 1 1 4 2.5a1.5 1.5 0 0 1 0 3z" fill="#111"/></svg>214 Kestrel Ridge Lane, Vlakfontein Rise, Pretoria</span>
      </p>
      <p class="credentials">Advocate of the High Court &nbsp;|&nbsp; Mediator &nbsp;|&nbsp; Arbitrator &nbsp;|&nbsp; <b>LLB | LLM (Cum Laude)</b> &nbsp;|&nbsp; Cert. Dir (KWBFE) Oct. 2021 &nbsp;|&nbsp; Chartered Secretary (TREPX) Nov. 2021 &nbsp;|&nbsp; Member of In-House Counsel Guild of Southern Africa</p>
    </footer>
  </section>

  <div class="hero-mark wordmark">
    <span class="initials">PS</span>
    <span class="name">Entity Frameworks</span>
  </div>

  <section class="signature">
    <div class="wordmark">
      <span class="initials">PS</span>
      <span>Entity Frameworks</span>
    </div>
    <div class="divider"></div>
    <div class="details">
      <p class="trading-name">P Sandovik t/a <b>PS Entity Frameworks</b></p>
      <p class="row">
        <span class="contact"><svg width="9" height="9" viewBox="0 0 10 10"><circle cx="5" cy="5" r="4.4" fill="none" stroke="#111" stroke-width=".9"/><path d="M3.4 2.8l1 1-.5.6a3 3 0 0 0 1.7 1.7l.6-.5 1 1-.7.7C5 7.1 2.9 5 3 3.5z" fill="#111"/></svg>+27 71 592 6604</span>
        <span class="contact"><svg width="10" height="8" viewBox="0 0 10 8"><rect x=".5" y=".5" width="9" height="7" rx="1" fill="none" stroke="#111" stroke-width=".9"/><path d="M.8 1l4.2 3.4L9.2 1" fill="none" stroke="#111" stroke-width=".9"/></svg>peter@kwellbrandt.com</span>
      </p>
      <p class="row"><span class="contact"><svg width="8" height="10" viewBox="0 0 8 11"><path d="M4 0a4 4 0 0 0-4 4c0 3 4 7 4 7s4-4 4-7a4 4 0 0 0-4-4zm0 5.5A1.5 1.5 0 1 1 4 2.5a1.5 1.5 0 0 1 0 3z" fill="#111"/></svg>214 Kestrel Ridge Lane, Vlakfontein Rise, Pretoria</span></p>
      <p class="row"><span class="contact"><svg width="9" height="9" viewBox="0 0 9 9"><rect width="9" height="9" rx="1" fill="#111"/></svg>http://www.prolink.example/in/petersandovik/</span></p>
      <p class="fine">Advocate of the High Court &nbsp;|&nbsp; Mediator &nbsp;|&nbsp; Arbitrator &nbsp;|&nbsp; <b>LLB | LLM (Cum Laude)</b><br>
      Cert. Dir (KWBFE) Oct. 2021 &nbsp;|&nbsp; Chartered Secretary (TREPX) Nov. 2021<br>
      Member of In-House Counsel Guild of Southern Africa</p>
    </div>
  </section>
</body>
</html>
```